Need Exciting Podcast Cover Art Design for New Show!

We need a podcast art design for our new show. It is called "Spark Forge Climb a Label" and we've interviewed hundreds of proven online entrepreneurs and experts and asked them to share their best advice for starting an e-commerce product-based brand. I don't have a color palette however, I like Blue (but I'm open to your suggestion). I want a podcast cover art that stands out, jumps out when people are browsing.

Target Market(s)

People who have a product idea and want to sell it online directly to the consumer

Font styles to use
Sans Serif

Requirements
Must have
• It should have the name: The Spark Forge Climb a Label Show and the most important words in the title/they should stand out are Spark Forge Climb
Nice to have
• I want something simple yet I want it to pop out. For instance, if you use blue, add a hint of color to make it pop.

```html
<!DOCTYPE html>
<html lang="en">
<head>
<meta charset="utf-8">
<title>The Spark Forge Climb a Label Show — Podcast Cover</title>
<link rel="stylesheet" href="https://fonts.googleapis.com/css2?family=Oswald:wght@700&display=swap">
<style>
  :root {
    --blue-deep: #0026ff;
    --blue-mid: #0070ff;
    --blue-sky: #00bfff;
    --arrow-green: #1aff00;
    --title-white: #ffffff;
    --glow-navy: #001a8c;
    --figure-navy: #002350;
  }
  html, body {
    margin: 0;
    padding: 0;
    width: 1200px;
    height: 1200px;
    overflow: hidden;
  }
  .cover {
    display: block;
    width: 1200px;
    height: 1200px;
  }
  .cover-title {
    font-family: "Oswald", "Arial Narrow", sans-serif;
    font-weight: 700;
    fill: var(--title-white);
    filter: url(#title-glow);
  }
  .title-small { font-size: 95px; }
  .title-main { font-size: 262px; }
</style>
</head>
<body>
<svg class="cover" viewBox="0 0 1200 1200" xmlns="http://www.w3.org/2000/svg">
  <defs>
    <linearGradient id="sky-gradient" x1="0" y1="0" x2="1" y2="1">
      <stop offset="0" stop-color="var(--blue-deep)"/>
      <stop offset="0.35" stop-color="var(--blue-deep)"/>
      <stop offset="0.65" stop-color="var(--blue-mid)"/>
      <stop offset="0.85" stop-color="var(--blue-sky)"/>
      <stop offset="1" stop-color="var(--blue-sky)"/>
    </linearGradient>
    <linearGradient id="figures-gradient" x1="0" y1="1" x2="1" y2="0">
      <stop offset="0" stop-color="#ffffff" stop-opacity="0.55"/>
      <stop offset="1" stop-color="var(--figure-navy)" stop-opacity="0.75"/>
    </linearGradient>
    <filter id="title-glow" x="-20%" y="-20%" width="140%" height="140%">
      <feDropShadow dx="0" dy="0" stdDeviation="14" flood-color="var(--glow-navy)" flood-opacity="0.6"/>
    </filter>
  </defs>

  <rect class="background" width="1200" height="1200" fill="url(#sky-gradient)"/>

  <polygon class="growth-arrow" fill="var(--arrow-green)"
    points="51,885 1014,367 973,300 1159,312 1089,485 1048,419 84,937"/>

  <g class="climbers" role="img" aria-label="Illustration of two stick figures climbing up the green arrow">
    <rect x="65" y="640" width="208" height="236" rx="30" fill="url(#figures-gradient)"/>
  </g>

  <text class="cover-title title-small" x="540" y="184" textLength="143" lengthAdjust="spacingAndGlyphs">THE</text>
  <text class="cover-title title-main" x="292" y="438" textLength="635" lengthAdjust="spacingAndGlyphs">SPARK</text>
  <text class="cover-title title-main" x="297" y="690" textLength="618" lengthAdjust="spacingAndGlyphs">FORGE</text>
  <text class="cover-title title-main" x="294" y="940" textLength="630" lengthAdjust="spacingAndGlyphs">CLIMB</text>
  <text class="cover-title title-small" x="298" y="1054" textLength="616" lengthAdjust="spacingAndGlyphs">A LABEL SHOW</text>
</svg>
</body>
</html>
```